8x8 Social Media Ad - Harbor Summit Expo

Attention Real Estate Agents
Please join us for our
Quarterly Real Estate Training Expo
The 2nd Saturday of February, May, August and November
Our Next Training Expo is _________________________________
From 9 am to 1 pm
at
Marlowe Suites Fernridge Station
4187 Copperleaf Lane, Greenbelt, MD 20770
Scheduled Speakers
9:00 am - Desmond Pryce - Orientation
9:30 am - Terrell Oakes - Multiple Income Streams / Keystone Track
10:00 am - Lorna Beckett - Marketing though Social Media
10:45 am - Raul Denning - Generating Business through Kelp-Nest
11:30 am - Tunde Adesemi - Real Estate Investing
12:15 pm - Marcus Oyelowo - (Main Speaker) Training Topic TBA
For more information call Desmond Pryce at (240) 555-0192 or email dpryce@harborsummithomes.example

```html
<!DOCTYPE html>
<html lang="en">
<head>
<meta charset="utf-8">
<title>Harbor Summit Expo – Quarterly Real Estate Training Expo</title>
<link href="https://fonts.googleapis.com/css2?family=Archivo:wght@400;600;700;800&display=swap" rel="stylesheet">
<style>
  :root {
    --teal: #0b8e9a;
    --ink: #0a0a0a;
    --white: #ffffff;
    --panel: #f1f1f1;
    --band: #000000;
    --backdrop: #abc4cf;
    --rule: #d6d6d6;
  }
  * { box-sizing: border-box; margin: 0; padding: 0; }
  html, body { width: 1200px; height: 1194px; overflow: hidden; }
  body {
    background: var(--backdrop);
    font-family: "Archivo", Arial, sans-serif;
    color: var(--ink);
    position: relative;
  }
  .ad {
    position: absolute; left: 107px; top: 104px;
    width: 986px; height: 986px;
    background: var(--white);
    overflow: hidden;
  }
  .headline-box {
    position: absolute; left: 50px; top: 40px;
    width: 355px; height: 77px;
    background: var(--teal);
    color: var(--white);
    font-weight: 700; font-size: 84px; line-height: 77px;
    letter-spacing: -0.055em; text-align: center;
  }
  .headline-sub {
    position: absolute; left: 50px; top: 118px; width: 360px;
    font-weight: 700; font-size: 43px; letter-spacing: -0.05em; line-height: 48px;
  }
  .intro {
    position: absolute; left: 417px; top: 39px;
    width: 521px; height: 128px;
    background: var(--panel);
    padding: 14px 10px 0 23px;
    font-size: 28.5px; line-height: 34px; letter-spacing: -0.055em;
  }
  .intro strong { color: var(--teal); font-weight: 700; }
  .next-expo {
    position: absolute; left: 48px; top: 218px;
    font-weight: 700; font-size: 38px; letter-spacing: -0.05em;
  }
  .next-expo span { color: var(--teal); }
  .divider { position: absolute; left: 48px; top: 319px; width: 509px; height: 2px; background: var(--rule); }
  .details { position: absolute; left: 48px; top: 340px; font-size: 29px; letter-spacing: -0.055em; line-height: 29px; }
  .detail { position: relative; padding-left: 35px; }
  .detail + .detail { margin-top: 9px; }
  .detail svg { position: absolute; left: 0; top: 4px; width: 22px; height: 22px; }
  .house-visual {
    position: absolute; left: 570px; top: 157px; width: 416px; height: 314px;
    background: radial-gradient(ellipse at 60% 55%, #a5583f 0%, #c58c72 35%, #e6e2de 70%, #ffffff 95%);
  }
  .speakers-band {
    position: absolute; left: 0; top: 471px; width: 986px; height: 354px;
    background: var(--band);
  }
  .speakers-title {
    position: absolute; top: 13px; width: 100%; text-align: center;
    color: var(--white); font-weight: 700; font-size: 28px; letter-spacing: -0.05em;
  }
  .speaker {
    position: absolute; width: 290px; height: 128px;
    background: var(--white); border: 2px solid var(--teal);
    display: flex;
  }
  .speaker-photo { width: 106px; height: 100%; flex: none; background: linear-gradient(160deg, #6b6b6b, #2b2b2b); }
  .speaker-info { padding: 10px 0 0 13px; letter-spacing: -0.05em; }
  .speaker-time { font-size: 21px; line-height: 26px; }
  .speaker-name { font-size: 21px; font-weight: 700; line-height: 28px; }
  .speaker-topic { font-size: 16.5px; line-height: 19px; margin-top: 2px; }
  .row1 { top: 57px; } .row2 { top: 199px; }
  .col1 { left: 45px; } .col2 { left: 347px; } .col3 { left: 648px; }
  .footer {
    position: absolute; left: 0; top: 825px; width: 986px; height: 161px;
    background: var(--panel);
  }
  .brand {
    position: absolute; left: 70px; top: 52px; width: 270px;
    color: var(--teal); font-weight: 800; font-size: 27px; line-height: 30px;
    letter-spacing: -0.03em; text-align: center;
  }
  .footer-rule { position: absolute; left: 377px; top: 31px; width: 1px; height: 96px; background: #c8c8c8; }
  .contact {
    position: absolute; left: 410px; top: 34px;
    font-weight: 700; font-size: 25px; line-height: 31px; letter-spacing: -0.055em;
  }
  .contact span { color: var(--teal); }
</style>
</head>
<body>
  <main class="ad">
    <div class="headline-box">Attention</div>
    <div class="headline-sub">Real Estate Agents</div>
    <p class="intro">Please join us for our <strong>Quarterly Real Estate Training Expo!</strong> The 2nd Saturday of February, May, August and November</p>

    <h2 class="next-expo">Our Next <span>Training Expo</span> is</h2>
    <div class="divider"></div>
    <div class="details">
      <div class="detail">
        <svg viewBox="0 0 24 24"><circle cx="12" cy="12" r="12" fill="var(--teal)"/><path d="M8.2 6.2l2 2.4-1.2 1.6c.8 1.8 2.2 3.2 4 4l1.6-1.2 2.4 2-1.3 2c-4.4-.3-9.2-5-9.5-9.5z" fill="#fff"/></svg>
        9 am to 1 pm
      </div>
      <div class="detail">
        <svg viewBox="0 0 24 24"><path d="M12 1C7 1 3.5 4.7 3.5 9.3 3.5 15 12 23 12 23s8.5-8 8.5-13.7C20.5 4.7 17 1 12 1z" fill="var(--teal)"/><circle cx="12" cy="9.4" r="3.4" fill="#fff"/></svg>
        Marlowe Suites Fernridge Station 4187<br>Copperleaf Lane, Greenbelt, MD 20770
      </div>
    </div>

    <div class="house-visual" role="img" aria-label="Modern two-storey house with timber cladding, glass walls and landscaped garden"></div>

    <section class="speakers-band">
      <h3 class="speakers-title">Scheduled Speakers</h3>
      <div class="speaker row1 col1"><div class="speaker-photo" role="img" aria-label="Portrait of Desmond Pryce"></div><div class="speaker-info"><div class="speaker-time">9:00 am</div><div class="speaker-name">Desmond Pryce</div><div class="speaker-topic">Orientation</div></div></div>
      <div class="speaker row1 col2"><div class="speaker-photo" role="img" aria-label="Portrait of Terrell Oakes"></div><div class="speaker-info"><div class="speaker-time">9:30 am</div><div class="speaker-name">Terrell Oakes</div><div class="speaker-topic">Multiple Income<br>Streams / Keystone Track</div></div></div>
      <div class="speaker row1 col3"><div class="speaker-photo" role="img" aria-label="Portrait of Lorna Beckett"></div><div class="speaker-info"><div class="speaker-time">10:00 am</div><div class="speaker-name">Lorna Beckett</div><div class="speaker-topic">Marketing though<br>Social Media</div></div></div>
      <div class="speaker row2 col1"><div class="speaker-photo" role="img" aria-label="Portrait of Raul Denning"></div><div class="speaker-info"><div class="speaker-time">10:45 am</div><div class="speaker-name">Raul Denning</div><div class="speaker-topic">Generating Business<br>through Kelp-Nest</div></div></div>
      <div class="speaker row2 col2"><div class="speaker-photo" role="img" aria-label="Portrait of Tunde Adesemi"></div><div class="speaker-info"><div class="speaker-time">11:30 am</div><div class="speaker-name">Tunde Adesemi</div><div class="speaker-topic">Real Estate Investing</div></div></div>
      <div class="speaker row2 col3"><div class="speaker-photo" role="img" aria-label="Portrait of Marcus Oyelowo"></div><div class="speaker-info"><div class="speaker-time">12:15 pm</div><div class="speaker-name">Marcus Oyelowo</div><div class="speaker-topic">Training Topic TBA</div></div></div>
    </section>

    <footer class="footer">
      <div class="brand">Harbor Summit<br>Realty Group</div>
      <div class="footer-rule"></div>
      <div class="contact">
        For more information<br>
        Call Desmond Pryce at <span>(240) 555-0192</span> or<br>
        Email <span>dpryce@harborsummithomes.example</span>
      </div>
    </footer>
  </main>
</body>
</html>
```